Real Estate Entrepreneur needs a business card

I am a real estate entrepreneur, I buy houses for investment purposes, I act as a real estate agent representing buyers and sellers in residential home transactions, I am a contractor that does a wide range of home repairs and construction. I'd like a design that can stick with me through the years as my business grows and morphs to fit any niche I decide to pursue as markets change.

Target Market(s)

Anyone with interest that may be related to real estate.

Industry/Entity Type

Real Estate

Contact Information for Business Card

A card that stands out and doesn't put me in any one box. My business will evolve over time and I need a card that can stay relevant.

Colors

Designer to choose colors to be used in the design.

Requirements
Must have
• Character
Nice to have
• I'm open
Should not have
• Cliche houses and hammers

```html
<!DOCTYPE html>
<html lang="en">
<head>
<meta charset="utf-8">
<title>Cole Harper – Business Card</title>
<link rel="stylesheet" href="https://fonts.googleapis.com/css2?family=Lato:wght@400;700&family=Montserrat:wght@500&display=swap">
<style>
  :root {
    --navy: #1c1856;
    --paper: #ffffff;
    --ink: #111111;
    --backdrop: #5a5a5a;
    --backdrop-dark: #2e2e2e;
  }
  * { box-sizing: border-box; margin: 0; padding: 0; }
  html, body { width: 1200px; height: 895px; overflow: hidden; }
  body {
    background: linear-gradient(180deg, var(--backdrop) 0%, var(--backdrop-dark) 100%);
    font-family: "Lato", Arial, sans-serif;
    position: relative;
  }
  .card {
    position: absolute;
    top: 97px;
    width: 400px;
    height: 700px;
    box-shadow: 0 10px 30px rgba(0,0,0,.35);
  }
  .card--back  { left: 160px; background: var(--navy); color: var(--paper); }
  .card--front { left: 640px; background: var(--paper); color: var(--ink); }

  .frame { position: absolute; left: 60px; top: 110px; width: 300px; height: 300px; }
  .frame svg { display: block; }

  .title-block { position: absolute; left: 112px; top: 78px; }
  .title-block .role {
    font-size: 17px; letter-spacing: .3px; line-height: 1;
  }
  .title-block .name {
    font-family: "Montserrat", Arial, sans-serif;
    font-weight: 500; font-size: 44px; line-height: 1; margin-top: 4px;
    letter-spacing: .5px;
  }
  .card--back .role { color: var(--paper); }
  .card--back .name { color: var(--ink); }
  .card--front .name { color: var(--navy); }

  .services {
    position: absolute; left: 40px; top: 440px; width: 330px;
    list-style: none; font-size: 15.5px; line-height: 1.45; letter-spacing: .2px;
  }
  .services li::before { content: "- "; }
  .services li { margin-bottom: 2px; }

  .contact { position: absolute; left: 40px; top: 440px; }
  .contact .icons { display: flex; gap: 12px; margin-bottom: 8px; }
  .contact .phone { font-size: 27px; letter-spacing: 1.5px; line-height: 1.2; }
  .contact .email { font-size: 19px; line-height: 1.3; }

  .rule { position: absolute; left: 40px; width: 72px; height: 3px; top: 575px; }
  .card--back .rule { background: var(--ink); }
  .card--front .rule { background: var(--navy); }

  .web { position: absolute; left: 40px; top: 610px; font-weight: 700; font-size: 22px; letter-spacing: .5px; }
</style>
</head>
<body>

<section class="card card--back">
  <div class="frame">
    <svg width="300" height="300" viewBox="0 0 300 300">
      <path d="M1 60 V299 H299 V1 H150 M1 60 V45 M40 1 H1" fill="none" stroke="var(--ink)" stroke-width="2"/>
    </svg>
  </div>
  <div class="title-block">
    <p class="role">Real Estate Enterpreneure</p>
    <p class="name">COLE HARPER</p>
  </div>
  <ul class="services">
    <li>Buy houses for investment purposes</li>
    <li>Act as a real estate agent representing buyers and sellers in residential home transactions</li>
    <li>A contractor that does a wide range of home repairs and construction.</li>
  </ul>
  <div class="rule"></div>
  <p class="web">www.ColeHarperRE.com</p>
</section>

<section class="card card--front">
  <div class="frame">
    <svg width="300" height="300" viewBox="0 0 300 300">
      <path d="M1 60 V299 H299 V1 H150 M1 60 V45 M40 1 H1" fill="none" stroke="var(--navy)" stroke-width="2"/>
    </svg>
  </div>
  <div class="title-block">
    <p class="role">Real Estate Enterpreneure</p>
    <p class="name">COLE HARPER</p>
  </div>
  <div class="contact">
    <div class="icons">
      <svg width="22" height="22" viewBox="0 0 24 24" aria-label="Phone">
        <path d="M6.6 10.8a15 15 0 0 0 6.6 6.6l2.2-2.2a1 1 0 0 1 1-.25 11.4 11.4 0 0 0 3.6.6 1 1 0 0 1 1 1V20a1 1 0 0 1-1 1A17 17 0 0 1 3 4a1 1 0 0 1 1-1h3.5a1 1 0 0 1 1 1c0 1.25.2 2.45.6 3.6a1 1 0 0 1-.25 1z" fill="var(--navy)"/>
      </svg>
      <svg width="24" height="22" viewBox="0 0 24 20" aria-label="Email">
        <rect x="1" y="2" width="22" height="16" rx="2" fill="var(--navy)"/>
        <path d="M2 4 L12 11 L22 4" fill="none" stroke="var(--paper)" stroke-width="1.6"/>
      </svg>
    </div>
    <p class="phone">000 555 0142</p>
    <p class="email">Cole.Harper@mailbox.com</p>
  </div>
  <div class="rule"></div>
  <p class="web">www.ColeHarperRE.com</p>
</section>

</body>
</html>
```